Tree Pruning Website

We need a website for a tree Arborist, pruning company called Hollow Ridge Groundcare. We look after all types of trees, knock down trees and prune trees. Our target market is from domestic clients to government clients and everything in between.

We would like to see the use of our main colours which are orange and green

We are not looking forward in seeing a template that we have seen before but a unique template. We have designed 5 templates ourselves and we wish for the design community to take our designs to the next level.

We have also designed a template for things that **we are not** looking for (Version 4)

To make it fair for everyone, we are also not giving out any participation payments as we have had. One winner will take all of the payment!!!

I Have attached a image of the designs and a image of a tree.

We are just looking at the PSD file been developed. We have our own team who can slice the image up into a HTML format.

Target Market(s)

Everyone who needs to cut down a tree

Industry/Entity Type

Government

Requirements
Must have
• Logo on front page
A List of our services
jQuery slider on page
Phone Number on every page

```html
<!DOCTYPE html>
<html lang="en">
<head>
<meta charset="utf-8">
<title>Hollow Ridge Groundcare</title>
<link href="https://fonts.googleapis.com/css2?family=Jost:wght@400;500&family=Roboto:ital,wght@0,300;0,400;1,300;1,400&display=swap" rel="stylesheet">
<style>
:root{
  --bg-dark:#33352f;
  --frame-green:#a1cd78;
  --accent:#93c066;
  --accent-text:#7cae52;
  --hero-bg:#cfd9c9;
  --gallery-bg:#e3e9dc;
  --footer-main:#bcc9a8;
  --footer-sub:#cfe0b4;
  --ink:#333;
  --ink-soft:#555;
  --ghost:#dcdcdc;
  --white:#fff;
  --photo-sky:#8fa9c9;
  --photo-leaf:#8d8a4f;
}
*{margin:0;padding:0;box-sizing:border-box}
html,body{width:1000px;height:1200px;overflow:hidden;background:var(--bg-dark)}
body{position:relative;font-family:"Roboto",sans-serif;font-weight:300;color:var(--ink)}
.abs{position:absolute}
.nowrap{white-space:nowrap}
.top-strip{left:45px;top:0;width:913px;height:7px;background:var(--footer-sub)}
.brand{left:181px;top:15px;font-family:"Jost",sans-serif;font-weight:400;font-size:22px;line-height:24px;color:var(--white);letter-spacing:.8px;text-transform:uppercase;white-space:nowrap}
.header-phone{left:575px;top:30px;font-family:"Jost",sans-serif;font-weight:400;font-size:15px;color:var(--frame-green);letter-spacing:.6px}
.header-phone b{font-weight:400;color:var(--white)}
.frame{left:45px;top:71px;width:913px;height:1117px;background:var(--frame-green)}
.page{left:142px;top:81px;width:720px;height:992px;background:var(--white)}
.nav{right:36px;top:10px;display:flex;font-size:11px;font-weight:400;letter-spacing:.5px;color:var(--ink)}
.nav span{margin-left:40px}
.hero{left:29px;top:33px;width:662px;height:296px;background:var(--hero-bg)}
.photo{background:linear-gradient(160deg,var(--photo-sky) 0%,var(--photo-leaf) 45%,#e6e2cf 70%,#b9a97a 100%)}
.hero-photo{left:16px;top:15px;width:398px;height:264px}
.hero-title{right:15px;top:62px;text-align:right;font-size:30px;line-height:32px;letter-spacing:1.5px;color:var(--ink);font-weight:300}
.hero-text{right:15px;top:168px;text-align:right;font-size:9.5px;line-height:16px;color:var(--ink-soft);letter-spacing:.4px;white-space:nowrap}
.btn{background:var(--accent);color:var(--white);font-size:12.5px;font-weight:300;letter-spacing:.9px;height:26px;line-height:26px;padding:0 10px;white-space:nowrap}
.hero-btn{right:15px;top:233px}
.col{top:370px;width:215px}
.col h2{font-weight:300;font-size:25px;line-height:24px;letter-spacing:1.2px;color:var(--ink);margin-bottom:11px}
.col p{font-size:8.3px;line-height:12.2px;color:var(--ink);font-weight:400;white-space:nowrap}
.services{list-style:none;font-size:11.5px;line-height:17.5px;letter-spacing:.5px;margin:-4px 0 7px}
.services li::before{content:"›";font-weight:400;margin:0 8px 0 0}
.col-btn{top:549px}
.section-title{left:46px;top:602px;font-size:20px;letter-spacing:1.2px;font-weight:300}
.gallery{left:29px;top:632px;width:662px;height:183px;background:var(--gallery-bg)}
.gal-item{top:20px;width:147px}
.gal-photo{height:98px;margin-bottom:9px}
.gal-item p{font-size:8px;line-height:12px;font-weight:400;color:var(--ink);white-space:nowrap}
.gal-item p span{font-size:10px;font-weight:300}
.quote-title{left:46px;top:846px;font-size:26px;letter-spacing:1.2px;color:var(--ghost);font-weight:300}
.quote-lead{left:46px;top:879px;font-size:13px;letter-spacing:.5px;color:var(--accent-text);font-weight:400}
.quote-body{left:46px;top:900px;font-size:8.3px;line-height:12.2px;font-weight:400;white-space:nowrap}
.quote-name{right:60px;top:940px;font-size:8.5px;font-style:italic;font-weight:400}
.footer{left:142px;top:1073px;width:720px;height:55px;background:var(--footer-main)}
.footer-address{left:44px;top:18px;font-size:7.5px;line-height:12px;color:var(--white);letter-spacing:.3px;text-transform:uppercase;font-weight:400}
.footer-address b{font-weight:400;text-transform:none;color:var(--ink)}
.networks{left:527px;top:20px;font-size:8px;color:var(--white);font-weight:400}
.net{top:13px;width:25px;height:25px}
.footer-nav{left:142px;top:1130px;width:720px;height:28px;background:var(--footer-sub);font-size:7.5px;font-weight:400;letter-spacing:.4px;color:var(--ink-soft)}
.footer-nav .links{top:9px;display:flex;white-space:nowrap}
.footer-nav .links span{margin-right:17px}
</style>
</head>
<body>
<div class="abs top-strip"></div>
<div class="abs brand">Hollow Ridge<br>Groundcare</div>
<div class="abs header-phone">CONTACT US NOW: <b>08 7420 3150</b></div>

<div class="abs frame"></div>
<main class="abs page">
  <nav class="abs nav"><span>Home</span><span>About us</span><span>Our Services</span><span>Get a Quote</span><span>Contact Us</span></nav>

  <section class="abs hero">
    <div class="abs photo hero-photo" role="img" aria-label="Looking up into tall pale-barked eucalyptus trees against a blue sky"></div>
    <h1 class="abs hero-title">Lorem ipsum<br>dolorsitamet<br>consectetuer</h1>
    <p class="abs hero-text">Adipiscing elit, seddiam nonummy nibheuis<br>tincidunt ut laoreet doloremagna aliquamer<br>dolor mag ater wisi enim ad minim enam</p>
    <div class="abs btn hero-btn">Know more</div>
  </section>

  <section class="abs col" style="left:46px">
    <h2>When pruning<br>needed</h2>
    <p>Adipiscing elit, seddiam nonummy nibheuis<br>tincidunt utlaoreet doloremagna aliquamer oremi<br>ipsum dolor sit amet, consectetuer a dipiscingeli<br>sed diam nonummy nibh euismod tinci dunt utao<br>reet dolore magna aliquam erat volutpat. Utwisie<br>nim adminim veniam, quis nostrud exerci tationu<br>lamcorpe dolor mag ater wisi enim ad minim ena<br>Uwisienim adminim veniam, quis nostrud exercie<br>lamcorpe dolor mag ater wisie</p>
  </section>
  <section class="abs col" style="left:263px">
    <h2>Why<br>need us</h2>
    <p>Adipiscing elit, seddiam nonummy nibheuis<br>tincidunt utlaoreet doloremagna aliquamer oremi<br>ipsum dolor sit amet, consectetuer a dipiscingeli<br>sed diam nonummy nibh euismod tinci dunt utao<br>reet dolore magna aliquam erat volutpat. Utwisie<br>nim adminim veniam, quis nostrud exerci tationu<br>lamcorpe dolor mag ater wisi enim ad minim ena<br>Uwisienim adminim veniam, quis nostrud exercie<br>lamcorpe dolor mag ater wisie</p>
  </section>
  <section class="abs col" style="left:480px">
    <h2>Our<br>Services</h2>
    <ul class="services"><li>Tree Pruning</li><li>Dangerous Tree Removal</li><li>Tree Trimming</li><li>Tree Shaping</li></ul>
    <p>Denim adminim veniam, quis nostrud exerci tatio<br>lamcorpe dolor mag ater wisi enim ad minim ena<br>wisienim adminim veniam</p>
  </section>
  <div class="abs btn col-btn" style="left:46px">Know more</div>
  <div class="abs btn col-btn" style="left:263px">Read our testimonials</div>
  <div class="abs btn col-btn" style="left:481px">Know more</div>

  <h2 class="abs section-title">Our Project Gallery</h2>
  <section class="abs gallery">
    <div class="abs gal-item" style="left:17px"><div class="photo gal-photo" role="img" aria-label="Pale eucalyptus trunks reaching into the canopy"></div><p><span>Adipiscing elit, sediam</span> nonumye<br>tincidunt utlaoreet doremagna aliquiet<br>ipsum dolor sit amet...</p></div>
    <div class="abs gal-item" style="left:177px"><div class="gal-photo" style="background:linear-gradient(135deg,#4d6fae 0%,#6f7f5a 55%,#b6604f 100%)" role="img" aria-label="Arborist cutting a trunk with a chainsaw"></div><p><span>Adipiscing elit, sediam</span> nonumye<br>tincidunt utlaoreet doremagna aliquiet<br>ipsum dolor sit amet...</p></div>
    <div class="abs gal-item" style="left:338px"><div class="gal-photo" style="background:linear-gradient(180deg,#6a9ad6,#8fb1dc 60%,#4a4536)" role="img" aria-label="Heavily pruned bare branches against a blue sky"></div><p><span>Adipiscing elit, sediam</span> nonumye<br>tincidunt utlaoreet doremagna aliquiet<br>ipsum dolor sit amet...</p></div>
    <div class="abs gal-item" style="left:499px"><div class="gal-photo" style="background:linear-gradient(90deg,#7a6a52,#9b8a6e 40%,#3f66a8 60%,#5b7fbf)" role="img" aria-label="Arborist in an elevated work platform beside a large trunk"></div><p><span>Adipiscing elit, sediam</span> nonumye<br>tincidunt utlaoreet doremagna aliquiet<br>ipsum dolor sit amet...</p></div>
  </section>

  <h2 class="abs quote-title">What do our clients say about us...</h2>
  <p class="abs quote-lead">They have done a great clean job, they deserve to be called the real professionals...</p>
  <p class="abs quote-body">Adipiscing elit, seddiam nonummy nibheuis tincidunt utlaoreet doloremagna aliquamer oremi ipsum dolor sit amet, consectetuer a dipiscingeli<br>sed diam nonummy nibh euismod tinci dunt utao reet dolore magna aliquam erat volutpat twisienim adminim veniam, quis nostrud exerci tatioadm<br>amcorpe dolor mag ater wisi enim ad minim enawi sienim adminim veniam, quis nostrud exercie lamcorpe dolor mag ater wisie...</p>
  <p class="abs quote-name">Daniel Mercer, CA</p>
</main>

<footer class="abs footer">
  <div class="abs footer-address">41 Larkspur Lane, Brambledale, WA 6090<br>Contact us now: <b>08 7420 3150</b> &nbsp;Fax: <b>08 7420 3151</b></div>
  <div class="abs networks">Our Networks</div>
  <div class="abs net" style="left:598px;background:#d0453a" aria-label="Social network link"></div>
  <div class="abs net" style="left:633px;background:#3b5b9a" aria-label="Social network link"></div>
  <div class="abs net" style="left:667px;background:#3fb0e6" aria-label="Social network link"></div>
</footer>
<div class="abs footer-nav">
  <div class="abs links" style="left:27px"><span>Home</span><span>About us</span><span>Our Services</span><span>Get a Quote</span><span>Contact Us</span></div>
  <div class="abs links" style="left:399px"><span>Tree Pruning</span><span>Dangerous Tree Removal</span><span>Tree Trimming</span><span style="margin-right:0">Tree Shaping</span></div>
</div>
</body>
</html>
```